Life Coach business needs a website design

I would like to get support in creating a website design. I will be starting a business as a life coach and I would like to start with something basic, but chic. It will be mainly a blog for now, but then I would like to start adding videos and hopefully podcast in the future. I took professional pictures of myself that I would like to include as a cover page. My main goal with this website is to capture the right audience by connecting with them through my mission, which is to embrace their inner greatness. I want to provide a sense of love, courage and authenticity when they open my website. I have a domain in Pagewell called :"Unfold the hidden bloom". I would be happy to discuss more of the details over the phone.

Target Market(s)

Young Adults (25-35)

Number of Pages Required

4 page

Colors

Designer to choose colors to be used in the design.

Requirements
Must have
• I am looking for a similar layout and vibe to these websites: https://tessawhorlby.com/meet-tessa/
• https://www.junopraskett.com
• My home page will include: About, Blog, Podcast, Subscribe.. (We can add icons of snapverra, clipvane and Boardlyn)
• I would like to have my name in the middle (Lunet), and include a note next to my picture "Your life is like a blank canvas and only you have the power to transform it into masterpiece. Take a chance and unfold the hidden bloom" L.T.

```html
<!DOCTYPE html>
<html lang="en">
<head>
<meta charset="utf-8">
<title>Unfold the hidden bloom</title>
<link href="https://fonts.googleapis.com/css2?family=Questrial&display=swap" rel="stylesheet">
<style>
:root{
  --ink:#1e1e1e;
  --muted:#9a9a9a;
  --line:#2a2a2a;
  --paper:#ffffff;
  --hero-a:#5c5a55;
  --hero-b:#8a8178;
  --skin:#c9a48f;
}
*{box-sizing:border-box;margin:0;padding:0}
html,body{width:1200px;height:3960px;overflow:hidden;background:var(--paper);color:var(--ink);font-family:"Questrial",Arial,sans-serif}
.page{position:relative;width:1200px;height:3960px}
.abs{position:absolute}
.photo{display:block}

.site-header .logo{left:161px;top:36px;font-size:31px;letter-spacing:.2px}
.main-nav{left:571px;top:46px;display:flex;gap:38px;font-size:17px}

.teaser{width:201px}
.teaser .photo{width:201px;height:172px}
.teaser .date{font-size:11.5px;color:var(--muted);margin-top:12px}
.teaser .title{font-size:11.5px;line-height:16px;margin-top:2px}

.hero{left:0;top:450px;width:1200px;height:484px;background:radial-gradient(ellipse at 62% 40%,var(--skin) 0%,#8f7a6d 25%,var(--hero-b) 45%,var(--hero-a) 100%);color:#fff;text-align:center}
.hero .welcome{position:absolute;top:142px;width:100%;font-size:23px}
.hero h1{position:absolute;top:182px;width:100%;font-weight:400;font-size:44px;letter-spacing:.5px}
.hero .btn{position:absolute;left:516px;top:258px;width:175px;height:55px;border:2px solid #fff;line-height:51px;font-size:17px}

.section-head{left:161px;width:866px;display:flex;justify-content:space-between;align-items:baseline}
.section-head h2{font-weight:400;font-size:31px}
.section-head a{color:var(--ink);font-size:16px;font-style:italic;text-decoration:underline}

.card-row{display:flex;gap:30px}
.card{width:273px}
.card .photo{width:273px;height:195px;position:relative}
.card .date{font-size:17px;color:var(--muted);margin-top:24px}
.card .title{font-size:16.5px;line-height:20px;margin-top:10px;width:265px}
.badge{position:absolute;left:50%;top:50%;transform:translate(-50%,-50%)}

.list-item{display:flex;gap:20px;width:420px}
.list-item .photo{width:176px;height:122px;flex:none}
.list-item .date{font-size:17px;color:var(--muted);margin-top:10px}
.list-item .title{font-size:16px;line-height:20px;margin-top:6px}

.newsletter{left:0;top:3250px;width:1200px;height:535px;background:linear-gradient(180deg,#b8a596 0%,#cbb7a6 45%,#a9a98c 100%)}
.newsletter .box{position:absolute;left:227px;top:97px;width:750px;height:318px;background:#fff;border:1px solid #bbb;text-align:center}
.newsletter h2{margin-top:78px;font-weight:400;font-size:34px;letter-spacing:.5px}
.newsletter p{margin-top:8px;font-size:17px}
.signup{display:flex;justify-content:center;gap:8px;margin-top:22px}
.signup .field{width:312px;height:44px;border:1px solid #888;text-align:left;padding-left:22px;line-height:42px;font-size:13px}
.signup .btn{width:141px;height:44px;border:2px solid var(--line);line-height:40px;font-size:16px}

.footer-nav{left:0;top:3827px;width:1200px;display:flex;justify-content:center;gap:36px;font-size:16px}
.social{left:0;top:3878px;width:1200px;display:flex;justify-content:center;gap:14px;font-size:12px;color:var(--ink)}
.social span::before{content:"";display:inline-block;width:7px;height:7px;border-radius:50%;background:var(--ink);margin-right:4px;vertical-align:1px}
.copyright{left:0;top:3918px;width:1200px;text-align:center;font-size:10px}
</style>
</head>
<body>
<div class="page">

<header class="site-header">
  <div class="abs logo">Unfold the hidden bloom</div>
  <nav class="abs main-nav"><span>About</span><span>Blogs</span><span>Videos</span><span>Podcast</span><span>Contact</span></nav>
</header>

<section class="abs teaser" style="left:161px;top:140px">
  <div class="photo" role="img" aria-label="Hand holding a small cloud against blue sky" style="background:linear-gradient(180deg,#4f8fc6,#bcd6ea 60%,#d9a88f)"></div>
  <div class="date">Jun 08, 2019</div><div class="title">Lorem ipsum dolor sit amet con-<br>sectetuer adipiscing elit</div>
</section>
<section class="abs teaser" style="left:387px;top:140px">
  <div class="photo" role="img" aria-label="Woman overlooking a lake and hills" style="background:linear-gradient(180deg,#8fa3b5,#4e6f60 55%,#6b6a3a)"></div>
  <div class="date">Jun 03, 2019</div><div class="title">Lorem ipsum dolor sit amet con-<br>sectetuer adipiscing elit</div>
</section>
<section class="abs teaser" style="left:613px;top:140px">
  <div class="photo" role="img" aria-label="Audience at a seminar" style="background:linear-gradient(180deg,#eeeeee,#d6d2cf 45%,#4d4a52)"></div>
  <div class="date">Jun 02, 2019</div><div class="title">Lorem ipsum dolor sit amet con-<br>sectetuer adipiscing elit</div>
</section>
<section class="abs teaser" style="left:839px;top:140px">
  <div class="photo" role="img" aria-label="Woman in a dress walking through a green field" style="background:linear-gradient(90deg,#5b6e3a,#5f8a86 45%,#7f9a4c)"></div>
  <div class="date">Jun 01, 2019</div><div class="title">Lorem ipsum dolor sit amet con-<br>sectetuer adipiscing elit</div>
</section>

<section class="abs hero" role="img" aria-label="Coach portrait among rocks by the sea">
  <div class="welcome">Welcome to Unfold the hidden bloom</div>
  <h1>BUSINESS AS A LIFE COACH</h1>
  <div class="btn">READ MORE</div>
</section>

<div class="abs section-head" style="top:985px"><h2>Recent Blogs</h2><a>View all blogs</a></div>
<div class="abs card-row" style="left:161px;top:1049px">
  <article class="card"><div class="photo" role="img" aria-label="Wooden letter blocks" style="background:linear-gradient(180deg,#5a4a3a,#a98e6c 50%,#4b3d30)"></div><div class="date">Jun 08, 2019</div><div class="title">Lorem ipsum dolor sit amet con-<br>sectetuer adipiscing elit</div></article>
  <article class="card"><div class="photo" role="img" aria-label="Smiling woman portrait" style="background:radial-gradient(circle at 65% 45%,#8a6a55,#f2efec 60%)"></div><div class="date">Jun 08, 2019</div><div class="title">Pellentesque faucibus Ut accum-<br>san ultricies elit Maecenas</div></article>
  <article class="card"><div class="photo" role="img" aria-label="Silhouette with raised arms at sunset" style="background:linear-gradient(180deg,#d98a4a,#f0b45a 45%,#2a1d18)"></div><div class="date">Jun 08, 2019</div><div class="title">Etiam nulla massa pharetra fa-<br>cilisis volutpat in imperdiet</div></article>
</div>

<div class="abs section-head" style="top:1413px"><h2>Most Popular Blogs</h2><a>View all blogs</a></div>
<div class="abs card-row" style="left:161px;top:1478px">
  <article class="card"><div class="photo" role="img" aria-label="Silhouette at purple sunset over water" style="background:linear-gradient(180deg,#c86fc7,#e08aa0 55%,#4a2d6b)"></div><div class="date">Jun 08, 2019</div><div class="title">Lorem ipsum dolor sit amet con-<br>sectetuer adipiscing elit</div></article>
  <article class="card"><div class="photo" role="img" aria-label="Two women in a coaching conversation" style="background:linear-gradient(90deg,#b46a4a,#e6e1da 50%,#c9b7a8)"></div><div class="date">Jun 08, 2019</div><div class="title">Pellentesque faucibus Ut accum-<br>san ultricies elit Maecenas</div></article>
  <article class="card"><div class="photo" role="img" aria-label="Person with arms raised under a pink sky" style="background:linear-gradient(180deg,#9a6f9a,#e9a27f 60%,#e58a6a)"></div><div class="date">Jun 08, 2019</div><div class="title">Etiam nulla massa pharetra fa-<br>cilisis volutpat in imperdiet</div></article>
</div>

<div class="abs section-head" style="left:166px;top:1843px"><h2>Latest Podcasts</h2><a>View More</a></div>
<div class="abs card-row" style="left:166px;top:1908px">
  <article class="card"><div class="photo" role="img" aria-label="Blurred figure against blue sky" style="background:linear-gradient(90deg,#7fb2d8,#8a7c70 55%,#111)"><svg class="badge" width="52" height="52" viewBox="0 0 52 52"><g fill="none" stroke="#fff" stroke-width="3"><path d="M14 34a16 16 0 1 1 24 0"/><path d="M19 29a10 10 0 1 1 14 0"/></g><circle cx="26" cy="24" r="4" fill="#fff"/><rect x="24" y="30" width="4" height="14" rx="2" fill="#fff"/></svg></div><div class="date">Jun 08, 2019</div><div class="title">Lorem ipsum dolor sit amet con-<br>sectetuer adipiscing elit</div></article>
  <article class="card"><div class="photo" role="img" aria-label="Blurred silhouette with raised arms in golden light" style="background:radial-gradient(circle at 50% 60%,#3a2a12,#e3a52a 55%,#f2c94a)"><svg class="badge" width="52" height="52" viewBox="0 0 52 52"><g fill="none" stroke="#fff" stroke-width="3"><path d="M14 34a16 16 0 1 1 24 0"/><path d="M19 29a10 10 0 1 1 14 0"/></g><circle cx="26" cy="24" r="4" fill="#fff"/><rect x="24" y="30" width="4" height="14" rx="2" fill="#fff"/></svg></div><div class="date">Jun 08, 2019</div><div class="title">Pellentesque faucibus Ut accum-<br>san ultricies elit Maecenas</div></article>
  <article class="card"><div class="photo" role="img" aria-label="Blurred group of friends outdoors" style="background:linear-gradient(90deg,#8a9a5a,#c86a9a 40%,#4f6fa0 70%,#8a8a6a)"><svg class="badge" width="52" height="52" viewBox="0 0 52 52"><g fill="none" stroke="#fff" stroke-width="3"><path d="M14 34a16 16 0 1 1 24 0"/><path d="M19 29a10 10 0 1 1 14 0"/></g><circle cx="26" cy="24" r="4" fill="#fff"/><rect x="24" y="30" width="4" height="14" rx="2" fill="#fff"/></svg></div><div class="date">Jun 08, 2019</div><div class="title">Etiam nulla massa pharetra fa-<br>cilisis volutpat in imperdiet</div></article>
</div>

<div class="abs section-head" style="top:2258px"><h2>Watch Our Videos</h2><a>View More</a></div>
<div class="abs card-row" style="left:161px;top:2322px">
  <article class="card"><div class="photo" role="img" aria-label="Blurred woman in light clothing" style="background:linear-gradient(90deg,#d6d6d6,#c8b4a4 55%,#dcdcdc)"><svg class="badge" width="52" height="52" viewBox="0 0 52 52"><circle cx="26" cy="26" r="26" fill="#fff"/><path d="M21 17l13 9-13 9z" fill="#111"/></svg></div><div class="date">Jun 08, 2019</div><div class="title">Lorem ipsum dolor sit amet con-<br>sectetuer adipiscing elit</div></article>
  <article class="card"><div class="photo" role="img" aria-label="Blurred portrait close-up" style="background:radial-gradient(ellipse at 50% 50%,#6a4e40,#a88a7a 35%,#f0eeec 70%)"><svg class="badge" width="52" height="52" viewBox="0 0 52 52"><circle cx="26" cy="26" r="26" fill="#fff"/><path d="M21 17l13 9-13 9z" fill="#111"/></svg></div><div class="date">Jun 08, 2019</div><div class="title">Pellentesque faucibus Ut accum-<br>san ultricies elit Maecenas</div></article>
  <article class="card"><div class="photo" role="img" aria-label="Blurred figure by the sea" style="background:linear-gradient(90deg,#c9dbe6,#e6d6cc 55%,#d5e3ea)"><svg class="badge" width="52" height="52" viewBox="0 0 52 52"><circle cx="26" cy="26" r="26" fill="#fff"/><path d="M21 17l13 9-13 9z" fill="#111"/></svg></div><div class="date">Jun 08, 2019</div><div class="title">Etiam nulla massa pharetra fa-<br>cilisis volutpat in imperdiet</div></article>
</div>

<article class="abs list-item" style="left:163px;top:2705px"><div class="photo" role="img" aria-label="Woman with arms raised at sunset" style="background:linear-gradient(180deg,#9a7a6a,#e39a5a 60%,#c76a3a)"></div><div><div class="date">Jun 08, 2019</div><div class="title">Lorem ipsum dolor sit amet<br>consectetuer adipiscing elit</div></div></article>
<article class="abs list-item" style="left:624px;top:2705px"><div class="photo" role="img" aria-label="Portrait of a smiling woman" style="background:linear-gradient(90deg,#2a2a30,#9a7a66 50%,#e8e8ea)"></div><div><div class="date">Jun 08, 2019</div><div class="title">Pellentesque faucibus Ut<br>accumsan ultricies</div></div></article>
<article class="abs list-item" style="left:163px;top:2869px"><div class="photo" role="img" aria-label="Joyful woman outdoors in sunlight" style="background:linear-gradient(90deg,#f2efe6,#b87a4a 55%,#c94a4a)"></div><div><div class="date">Jun 08, 2019</div><div class="title">Aliquam nec erat at purus<br>cursus interdum Vestibulu</div></div></article>
<article class="abs list-item" style="left:624px;top:2869px"><div class="photo" role="img" aria-label="Open hands under blue sky" style="background:linear-gradient(180deg,#4a7ac0,#9ac0e6 50%,#e0b898)"></div><div><div class="date">Jun 08, 2019</div><div class="title">Curabitur vel mi sit amet<br>magna malesuada</div></div></article>
<article class="abs list-item" style="left:163px;top:3035px"><div class="photo" role="img" aria-label="Hands framing a warm sunset" style="background:linear-gradient(90deg,#c98a6a,#e8b08a 50%,#a66a5a)"></div><div><div class="date">Jun 08, 2019</div><div class="title">Maecenas aliquet velit vel<br>turpis Mauris neque metus</div></div></article>
<article class="abs list-item" style="left:624px;top:3035px"><div class="photo" role="img" aria-label="Woman with raised arms in a field" style="background:linear-gradient(180deg,#e6ecf2,#c9a07a 60%,#8a6a3a)"></div><div><div class="date">Jun 08, 2019</div><div class="title">Donec iaculis diam a nisi ac-<br>cumsan viverra Duis sed</div></div></article>

<section class="abs newsletter" role="img" aria-label="Coach portrait in a meadow behind the signup panel">
  <div class="box">
    <h2>SUBSCRIBE TO OUR NEWSLETTER</h2>
    <p>Lorem ipsum dolor sit amet consectetuer adipis</p>
    <div class="signup"><div class="field">Email address</div><div class="btn">SIGN UP</div></div>
  </div>
</section>

<footer>
  <nav class="abs footer-nav"><span>ABOUT</span><span>BLOGS</span><span>VIDEOS</span><span>PODCAST</span><span>CONTACT</span></nav>
  <div class="abs social"><span>Snapverra</span><span>Friendora</span><span>Chirply</span><span>Boardlyn</span></div>
  <div class="abs copyright">© 2019 Company Name &nbsp;All right reserved</div>
</footer>

</div>
</body>
</html>
```